Wordpress Contest Brief I would like a WordPress theme designed

Industry / Entity Type

Financial consultancy / advisers

Current site is: http://www.quorvel-group.com

Looking for a complete overhaul of this site, we are after a clean modern look. Will require the ability to easily add, update and remove content, hence the WordPress design.
Example:
Add case studies
Industry documentation (downloadable brochures / flyers and such)

What we like from our current site is the colour the fonts and the logo (the city of London) we would like to have other city outlines (NYC and Tokyo, Hong Kong, Singapore).

The site will be used by our potential clients to get in contact and re-view the case studies, if possible would like to have a client login area where they can download our documents like NDA’s etc and T&C’s.

Task Outline

Create a Web Design (Coded - Design and coding required)
Designer must provide full implementation/coding depending on the platform chosen by the client (i.e. WordPress theme, HTML/CSS, bootstrap etc.)

Task Description

I need a full website built that must work on desktop and mobile. I can provide the London city skyline and the font file, which we have used. Some stock industrial photos will be required.

Requirements:

*Splash page
*What We Do
*How We do it
*Who Are We? To have the same information and links as the current site
*Why use us?
*Clients: To have the same information and links as the current site
*Partners: To have the same information and links as the current site
*Contact:

Target Market(s)

Financial institutions trading Equities, Futures, Options, Forex and Fixed Income.
Regulators, Exchanges, ECN’s
Buy side firms and Sell side firms

Industry/Entity Type

Financial

Coding

Coded - Design and coding required

Number of Pages Required

5+ page

Font styles to use
Sans Serif

Colors
f04a50

Requirements
Must have
• Splash page
• What We Do
• How We do it
• Who Are We? To have the same information and links as the current site
• Why use us?
• Clients: To have the same information and links as the current site
• Partners: To have the same information and links as the current site
• Contact:

```html
<!DOCTYPE html>
<html lang="en">
<head>
<meta charset="utf-8">
<title>Quorvel Group Advisers</title>
<link rel="stylesheet" href="https://fonts.googleapis.com/css2?family=Lato:wght@300;400;700;900&family=Orbitron:wght@500;700;900&display=swap">
<style>
:root{
  --red:#a8141b;
  --red-dark:#8e0f15;
  --ink:#1a1a1a;
  --text:#222;
  --grey-bg:#f3f3f3;
  --panel:#4a4a4a;
  --black:#000;
  --bar:#141414;
  --white:#fff;
  --muted:#8a8a8a;
}
*{box-sizing:border-box;margin:0;padding:0}
html,body{width:1200px;height:2651px;overflow:hidden}
body{position:relative;font-family:'Lato',sans-serif;color:var(--text);background:var(--white)}
.abs{position:absolute}
.display{font-family:'Orbitron',sans-serif}

/* header */
.site-header{position:absolute;left:0;top:0;width:1200px;height:100px;background:var(--white);border-bottom:4px solid var(--red)}
.brand{position:absolute;left:145px;top:34px;display:flex;align-items:center;gap:10px}
.brand-name{font-family:'Orbitron',sans-serif;font-weight:700;font-size:17px;letter-spacing:2px;color:var(--ink)}
.brand-dot{width:14px;height:14px;border-radius:50%;background:var(--red)}
.header-phone{position:absolute;right:142px;top:20px;display:flex;align-items:center;gap:8px;color:var(--red);font-size:17px;font-family:'Orbitron',sans-serif;font-weight:500}
.main-nav{position:absolute;right:142px;top:60px;display:flex;gap:24px;font-size:12.5px;font-weight:700;color:var(--ink)}

/* hero */
.hero{position:absolute;left:0;top:100px;width:1200px;height:520px;background:linear-gradient(180deg,#3b3d40 0%,#2a2c2f 45%,#1f2123 100%)}
.hero-title{position:absolute;top:168px;width:100%;text-align:center;font-family:'Orbitron',sans-serif;font-weight:900;font-size:44px;color:var(--white);letter-spacing:1px}
.hero-text{position:absolute;top:226px;left:140px;width:920px;text-align:center;font-size:20px;line-height:26px;color:var(--white)}
.btn-red{position:absolute;background:var(--red);color:var(--white);font-weight:900;font-size:15px;display:flex;align-items:center;justify-content:center;text-transform:uppercase}
.hero .btn-red{left:512px;top:296px;width:176px;height:42px}

/* section headings */
.section-heading{position:absolute;left:0;width:1200px;display:flex;align-items:center;justify-content:center;gap:14px;font-weight:300;font-size:37px;color:var(--ink)}
.section-heading .rule{width:68px;height:3px;background:var(--ink);border-radius:2px}

/* what we do */
.service{position:absolute;width:320px}
.service h3{font-family:'Orbitron',sans-serif;font-weight:700;font-size:17px;color:var(--ink);line-height:22px}
.service p{font-size:13.5px;line-height:17px;color:var(--text)}
.service.left{text-align:right}
.icon-circle{position:absolute;width:60px;height:60px;border-radius:50%;background:var(--red);display:flex;align-items:center;justify-content:center}
.hub-arc{position:absolute;left:456px;top:871px}
.hub-name{position:absolute;left:456px;top:955px;width:286px;text-align:center;font-family:'Orbitron',sans-serif;font-weight:700;font-size:13px;letter-spacing:1.5px;color:var(--ink)}

/* how we do it */
.band-grey{position:absolute;left:0;width:1200px;background:var(--grey-bg)}
.block-title{position:absolute;font-family:'Orbitron',sans-serif;font-weight:700;font-size:27px;color:var(--ink)}
.body-copy{position:absolute;font-size:12.8px;line-height:17.6px;color:var(--text)}
.btn-outline{position:absolute;border:2px solid var(--red);border-radius:6px;color:var(--red);font-weight:900;font-size:12.5px;display:flex;align-items:center;justify-content:center}
.photo{position:absolute}

/* who we are */
.member{position:absolute;top:1785px;width:200px;text-align:center}
.member .portrait{width:145px;height:145px;margin:0 auto;border-radius:50%;border:3px solid #e4e4e4;box-shadow:0 0 0 1px #ccc}
.member .name{margin-top:10px;font-family:'Orbitron',sans-serif;font-weight:700;font-size:14.5px;color:var(--red)}

/* why use us */
.why-links{position:absolute;left:145px;top:2228px;display:flex}
.why-link{display:flex;align-items:center;gap:10px;height:44px;padding-left:10px;border-left:3px solid var(--ink);margin-right:0;font-weight:900;font-size:14px;color:var(--red)}
.why-link:nth-child(1){width:208px}
.why-link:nth-child(2){width:207px}

/* contact panel */
.contact-panel{position:absolute;left:769px;top:2059px;width:288px;height:408px;background:var(--panel)}
.contact-tab{position:absolute;top:2059px;width:0;height:0;border-style:solid}
.contact-panel h2{position:absolute;top:24px;width:100%;text-align:center;font-family:'Orbitron',sans-serif;font-weight:700;font-size:19px;color:var(--white);letter-spacing:1px}
.field{position:absolute;left:11px;width:265px;height:34px;background:var(--white);font-size:12px;font-style:italic;color:#9a9a9a;padding:10px 8px}
.field.message{height:119px}
.contact-panel .btn-red{left:42px;top:337px;width:203px;height:41px;border-radius:3px;font-size:14.5px}

/* footer */
.site-footer{position:absolute;left:0;top:2318px;width:1200px;height:230px;background:var(--black)}
.footer-nav{position:absolute;left:145px;top:46px;display:flex;gap:22px;font-size:11px;font-weight:700;color:#bbb}
.footer-brand{position:absolute;left:145px;top:89px;display:flex;align-items:center;gap:12px}
.footer-brand span{font-family:'Orbitron',sans-serif;font-weight:500;font-size:13.5px;color:var(--white)}
.footer-brand i{display:block;width:400px;height:2px;background:linear-gradient(90deg,#fff,#fff 60%,rgba(255,255,255,0))}
.footer-details{position:absolute;left:145px;top:114px;font-size:10.5px;line-height:16px;color:var(--white);font-weight:700}
.footer-details .email{color:var(--red)}
.social{position:absolute;left:498px;top:116px;display:flex;gap:4px}
.social span{width:24px;height:24px;border-radius:50%;background:var(--white)}
.legal-bar{position:absolute;left:0;top:2548px;width:1200px;height:103px;background:var(--bar)}
.legal-bar p{position:absolute;left:145px;top:22px;width:912px;font-size:8.6px;line-height:11.5px;color:var(--muted)}
.legal-bar .email{color:var(--red)}
.legal-bar .copyright{position:absolute;right:143px;top:72px;font-size:8.6px;color:var(--muted)}
</style>
</head>
<body>

<header class="site-header">
  <div class="brand"><span class="brand-dot"></span><span class="brand-name">QUORVEL GROUP ADVISERS</span></div>
  <div class="header-phone">
    <svg width="22" height="22" viewBox="0 0 22 22"><circle cx="11" cy="11" r="9.5" fill="none" stroke="#a8141b" stroke-width="1.8"/><path d="M7.5 6.5c.6-.6 1.3-.5 1.7.1l.9 1.5c.3.5.2 1-.2 1.4l-.6.5c.5 1.2 1.5 2.2 2.7 2.7l.5-.6c.4-.4.9-.5 1.4-.2l1.5.9c.6.4.7 1.1.1 1.7-1 1-2.6 1.2-4.1.3-1.6-1-2.9-2.3-3.9-3.9-.9-1.5-.7-3.1.3-4.1z" fill="#a8141b"/></svg>
    <span>+44(0)20 7946 0182</span>
  </div>
  <nav class="main-nav"><span>Services &amp; Solutions</span><span>Why Us</span><span>Clients</span><span>Partners</span><span>About Us</span><span>Contact Us</span></nav>
</header>

<section class="hero" role="img" aria-label="Aerial black and white view of the London financial district with skyscrapers and river">
  <h1 class="hero-title">MiFID II</h1>
  <p class="hero-text">Quorvel Group Advisers can assess your technology, then provide solutions to solve potential issues to get you the correct Solution at the correct price point to achieve the desired results.</p>
  <div class="btn-red">&gt;&nbsp; Contact Us</div>
</section>

<!-- What we do -->
<h2 class="section-heading" style="top:718px"><span class="rule"></span>What We Do<span class="rule"></span></h2>

<div class="service left" style="left:194px;top:806px"><h3>Advice</h3><p>Board Level Advisory &amp; Programme Management</p></div>
<div class="icon-circle" style="left:523px;top:799px"><svg width="32" height="32" viewBox="0 0 32 32" fill="#fff"><path d="M16 6a8 8 0 0 0-4.8 14.4c.8.6 1.3 1.5 1.3 2.6h7c0-1.1.5-2 1.3-2.6A8 8 0 0 0 16 6z"/><rect x="12.5" y="24" width="7" height="2"/><rect x="13.5" y="27" width="5" height="2" rx="1"/><g stroke="#fff" stroke-width="1.6"><path d="M16 1v3M5 5l2 2M27 5l-2 2M1 14h3M28 14h3"/></g></svg></div>

<div class="service" style="left:686px;top:801px"><h3>Product Development</h3><p>Front-Office Trading Platforms &amp; Market Data Pre |At | Post Trade Risk</p></div>
<div class="icon-circle" style="left:618px;top:799px"><svg width="34" height="30" viewBox="0 0 34 30"><circle cx="12" cy="17" r="7" fill="none" stroke="#fff" stroke-width="4" stroke-dasharray="3 2.5"/><circle cx="12" cy="17" r="3" fill="#fff"/><circle cx="25" cy="8" r="5" fill="none" stroke="#fff" stroke-width="3" stroke-dasharray="2.5 2"/><circle cx="25" cy="8" r="1.8" fill="#fff"/></svg></div>

<div class="service left" style="left:86px;top:868px"><h3>Interim Management</h3><p>For Funds, Brokers, Vendors and IT<br>Service providers</p></div>
<div class="icon-circle" style="left:417px;top:867px"><svg width="36" height="26" viewBox="0 0 36 26" fill="#fff"><path d="M2 6l7-3 6 3-8 9-5-4z"/><path d="M34 6l-7-3-8 3 -5 5c-1 1 0 3 2 2l4-3 8 7 6-5z"/><path d="M8 16l3 3 2-1 2 2 2-1 2 2 2-1 3 1 2-2-7-6-3 2c-2 1-5 0-5-2z"/></svg></div>

<div class="service" style="left:793px;top:868px"><h3>Process Outsourcing</h3><p>RFI, RFP &amp; Independent tender<br>evaluations (assess before you invest)</p></div>
<div class="icon-circle" style="left:724px;top:867px"><svg width="34" height="34" viewBox="0 0 34 34"><circle cx="16" cy="18" r="12" fill="none" stroke="#fff" stroke-width="3"/><circle cx="16" cy="18" r="6.5" fill="none" stroke="#fff" stroke-width="3"/><circle cx="16" cy="18" r="2" fill="#fff"/><path d="M16 18L30 4" stroke="#fff" stroke-width="2.4"/><path d="M26 3h5v5z" fill="#fff"/></svg></div>

<div class="service left" style="left:49px;top:955px"><h3>Research</h3><p>Topical papers. White labelled and<br>sponsored articles</p></div>
<div class="icon-circle" style="left:376px;top:954px"><svg width="26" height="32" viewBox="0 0 26 32"><rect x="2" y="2" width="22" height="28" rx="2" fill="#fff"/><g stroke="#a8141b" stroke-width="2.2"><path d="M6 9h14M6 14h14M6 19h14M6 24h10"/></g></svg></div>

<div class="service" style="left:832px;top:956px"><h3>Training</h3><p>Trading Technology for compliance<br>and non technical staff</p></div>
<div class="icon-circle" style="left:763px;top:954px"><svg width="32" height="30" viewBox="0 0 32 30" fill="#fff"><rect x="4" y="18" width="5" height="9"/><rect x="12" y="13" width="5" height="14"/><rect x="20" y="8" width="5" height="19"/><path d="M2 27h28" stroke="#fff" stroke-width="2"/><path d="M3 14L12 7l6 4 9-8" fill="none" stroke="#fff" stroke-width="2.2"/><path d="M24 2h5v5z"/></svg></div>

<svg class="hub-arc" width="286" height="146" viewBox="0 0 286 146"><path d="M3 145 A140 140 0 0 1 283 145" fill="none" stroke="#a8141b" stroke-width="2.5"/></svg>
<div class="hub-name">QUORVEL GROUP<br>ADVISERS</div>

<!-- How we do it -->
<section class="band-grey" style="top:1124px;height:406px"></section>
<h2 class="block-title" style="left:145px;top:1198px">How We Do It</h2>
<p class="body-copy" style="left:145px;top:1238px;width:446px">Lorem ipsum dolor sit amet, consectetur adipiscing elit. In sollicitudin, tortor id imperdiet pretium, ipsum nisi lacinia felis, in suscipit justo magna quis dolor. Vestibulum libero dui, feugiat at sem volutpat, egestas vulputate neque. Etiam ut venenatis dui. Aenean posuere velit vel urna posuere, in efficitur justo commodo. Proin et enim luctus eros molestie viverra id sit amet mauris. Suspendisse tellus risus, commodo in tortor sed, iaculis faucibus ex. Nam pharetra nec est in elementum. Maecenas non gravida arcu. Maecenas fringilla nunc venenatis massa maximus, quis venenatis ligula faucibus. Vivamus mi turpis, volutpat quis augue et tristique varius.</p>
<div class="btn-outline" style="left:145px;top:1408px;width:134px;height:37px">&gt;&nbsp; LEARN MORE</div>
<div class="photo" style="left:611px;top:1195px;width:446px;height:263px;background:radial-gradient(ellipse at 58% 45%,#8cc63f 0%,#6e9a3a 16%,#7b7e82 30%,#5e6166 70%,#3d4044 100%)" role="img" aria-label="Finger pressing a green Solution key on a grey keyboard"></div>

<!-- Who we are -->
<h2 class="section-heading" style="top:1630px"><span class="rule"></span>Who We Are<span class="rule"></span></h2>
<p class="body-copy" style="left:145px;top:1705px;width:912px;text-align:center;line-height:19px">Since founding Quorvel Group Advisers in 2014 we have dedicated ourselves to the provision of services. What differentiates us from other advisers or consultancies is a genuine motivation to see our clients succeed. Today's technology allows our clients to take their knowledge to the market in ways that previous generations could only dream of. That's why QGA is dedicated to seeing you choose the right technology strategy, ensuring you maintain a competitive edge over your peers.</p>

<div class="member" style="left:147px"><div class="portrait" role="img" aria-label="Portrait photo of Tom Ashcroft" style="background:linear-gradient(160deg,#b9a79a,#c98d76 55%,#7a8a9a)"></div><div class="name">Tom Ashcroft</div></div>
<div class="member" style="left:382px"><div class="portrait" role="img" aria-label="Portrait photo of Daniel Harrow" style="background:linear-gradient(160deg,#e8e8e6,#c7a48e 55%,#3a3a3a)"></div><div class="name">Daniel Harrow</div></div>
<div class="member" style="left:616px"><div class="portrait" role="img" aria-label="Portrait photo of Peter Lindqvist" style="background:linear-gradient(160deg,#1f8a86,#c49477 55%,#2b2b2b)"></div><div class="name">Peter Lindqvist</div></div>
<div class="member" style="left:851px"><div class="portrait" role="img" aria-label="Black and white portrait photo of Maeve Ridley" style="background:linear-gradient(160deg,#d4d4d4,#8c8c8c 55%,#2e2e2e)"></div><div class="name">Maeve Ridley</div></div>

<!-- Why use us -->
<section class="band-grey" style="top:2085px;height:233px"></section>
<h2 class="block-title" style="left:145px;top:2124px">Why Use Us?</h2>
<p class="body-copy" style="left:145px;top:2158px;width:600px;line-height:19px">Lorem ipsum dolor sit amet, consectetur adipiscing elit. In sollicitudin, tortor id imperdiet pretium, ipsum nisi lacinia felis, in suscipit justo magna quis dolor. Vestibulum libero dui, feugiat at sem volutpat, egestas vulputate neque. Etiam ut venenatis dui. Aenean posuere velit vel urna posuere, in efficitur justo commodo et enim luctus eros.</p>
<div class="why-links">
  <div class="why-link"><svg width="30" height="26" viewBox="0 0 30 26"><rect x="2" y="6" width="26" height="18" rx="2" fill="#a8141b"/><path d="M10 6V3h10v3" fill="none" stroke="#a8141b" stroke-width="2.5"/></svg>CASE STUDIES</div>
  <div class="why-link"><svg width="36" height="26" viewBox="0 0 36 26" fill="#a8141b"><circle cx="14" cy="7" r="6"/><path d="M2 25c0-7 5-11 12-11s12 4 12 11z"/><circle cx="26" cy="8" r="4.5"/><path d="M24 14c6 0 10 3 10 10h-6c0-4-1.5-7-4-10z"/></svg>OUR CLIENTS</div>
  <div class="why-link"><svg width="28" height="28" viewBox="0 0 28 28"><circle cx="14" cy="14" r="12" fill="#a8141b"/><g fill="none" stroke="#fff" stroke-width="1.4"><ellipse cx="14" cy="14" rx="5" ry="12"/><path d="M2 14h24M4 8h20M4 20h20M14 2v24"/></g></svg>PARTNERS</div>
</div>

<!-- Footer -->
<footer class="site-footer">
  <nav class="footer-nav"><span>HOME</span><span>SERVICES &amp; SOLUTIONS</span><span>WHY US</span><span>CLIENTS</span><span>PARTNERS</span><span>ABOUT US</span><span>CONTACT US</span></nav>
  <div class="footer-brand"><span>Quorvel Group Advisers</span><i></i></div>
  <div class="footer-details">+44(0)20 7946 0182<br><span class="email">admin@quorvel-group.com</span><br>Suite 4 Harbour Court, Elmsworth, Northfield, NF12 3QT<br>Company No:08311736<br>VAT No: 4418207</div>
  <div class="social" aria-label="Social links"><span></span><span></span><span></span></div>
</footer>

<div class="contact-tab" style="left:757px;border-width:0 12px 22px 0;border-color:transparent #2f2f2f transparent transparent"></div>
<div class="contact-tab" style="left:1057px;border-width:0 0 22px 12px;border-color:transparent transparent transparent #2f2f2f"></div>
<aside class="contact-panel">
  <h2>CONTACT US</h2>
  <div class="field" style="top:54px">Name*</div>
  <div class="field" style="top:91px">Company Name</div>
  <div class="field" style="top:130px">Email*</div>
  <div class="field" style="top:167px">Phone</div>
  <div class="field message" style="top:204px">Message</div>
  <div class="btn-red">&gt;&nbsp; SEND A MESSAGE</div>
</aside>

<div class="legal-bar">
  <p>PRIVACY: QGA may receive names, e-mail addresses and other personally submitted details only when they are supplied by users through the optional QGA feedback form. This information is not gathered by QGA without the user's knowledge, active permission and participation. Submitted details allow QGA to respond to user enquiries and suggestions. QGA respects the privacy of visitors to this website and does not sell any personally identifiable information to third parties. To change or remove any information you have submitted to QGA, please contact Sales and Marketing by emailing <span class="email">admin@quorvel-group.com</span> or calling +44(0)20 7946 0182.</p>
  <div class="copyright">&copy;2017 Quorvel Group Advisers.</div>
</div>

</body>
</html>
```